We need a label design for our new company called Tovel Crest.
We are a company that is producing Pet Supplements, but the first products launched are going to be for the dogs.
First 3 products that we are launching are:
-Multivitamin (12 in 1)
-Probiotic
-Hip and Joint
We need label design for this three products that are going to be packed in the black plastic jar with the count of 120 pieces in each.
I am uploading our logo, but please do not pay attention to the colors of the logo as that can be changed and adjusted.
- Label dimensions are 2.25" x 11.125"
-Corner radius 0.125

Attached some badges with registrations and approvals.

```html
<!DOCTYPE html>
<html lang="en">
<head>
<meta charset="utf-8">
<title>Tovel Crest – Pet Supplement Labels</title>
<link href="https://fonts.googleapis.com/css2?family=Anton&family=Bebas+Neue&family=Montserrat:wght@400;500;700&display=swap" rel="stylesheet">
<style>
  :root {
    --green: #9ac93c;
    --orange: #f7941d;
    --red: #ed1c24;
    --panel: #f4f6f4;
    --ink: #333333;
    --ink-soft: #3f3f3f;
    --badge-navy: #27306b;
    --badge-light: #eef1f8;
    --white: #ffffff;
    --page: #ffffff;
  }
  * { box-sizing: border-box; margin: 0; padding: 0; }
  html, body { width: 800px; height: 1200px; overflow: hidden; background: var(--page); }
  body { position: relative; font-family: "Montserrat", sans-serif; color: var(--ink); }

  .label {
    position: absolute; left: 29px; width: 742px; height: 202px;
    background: var(--panel); overflow: hidden;
  }
  .label--probiotic { top: 190px; --accent: var(--green); }
  .label--joint { top: 500px; --accent: var(--orange); }
  .label--multi { top: 810px; --accent: var(--red); }

  .label__band-top { position: absolute; left: 0; top: 0; width: 100%; height: 38px; background: var(--accent); }
  .label__band-bottom {
    position: absolute; left: 0; bottom: 0; width: 100%; height: 30px; background: var(--accent);
    color: var(--white); font-weight: 700; font-size: 15px; letter-spacing: 3.2px;
    display: flex; align-items: center; justify-content: center;
  }

  .brand__mark { position: absolute; left: 257px; top: 4px; width: 40px; height: 40px; border-radius: 50%; background: #3d3d3d; }
  .brand__name {
    position: absolute; left: 305px; top: 12px; font-family: "Anton", sans-serif;
    font-size: 25px; line-height: 28px; color: var(--white); letter-spacing: 1.4px; white-space: nowrap;
  }

  .serving {
    position: absolute; left: 34px; top: 75px; width: 112px; height: 73px;
    border: 1.3px solid var(--ink-soft); font-size: 6.4px; font-weight: 700; color: var(--ink);
  }
  .serving__title { font-size: 10px; letter-spacing: 2.5px; font-weight: 500; padding: 2px 4px 1px; border-bottom: 1.3px solid var(--ink-soft); white-space: nowrap; }
  .serving table { width: 100%; border-collapse: collapse; }
  .serving th, .serving td { text-align: left; padding: 0 4px; line-height: 8.3px; }
  .serving th { border-bottom: 0.8px solid var(--ink-soft); font-size: 6.2px; padding-top: 1px; padding-bottom: 1px; }
  .serving th:first-child, .serving td:first-child { border-right: 1px solid var(--ink-soft); width: 55px; }
  .serving td:last-child { padding-left: 17px; }

  .art { position: absolute; }
  .art--dog { left: 185px; top: 53px; width: 80px; height: 117px; background: linear-gradient(180deg, #e8c58e 0%, #d9a862 60%, #efe4d2 100%); border-radius: 36px 36px 8px 8px; }
  .art--cat { left: 273px; top: 117px; width: 36px; height: 51px; background: linear-gradient(180deg, #b9b4aa 0%, #8d877d 60%, #dedad2 100%); border-radius: 14px 14px 6px 6px; }

  .title { position: absolute; font-family: "Anton", sans-serif; color: var(--accent); line-height: 1; white-space: nowrap; }
  .title--probiotic { left: 257px; top: 58px; font-size: 52px; letter-spacing: 0.8px; }
  .title--joint { left: 258px; top: 60px; font-size: 49px; letter-spacing: -0.3px; }
  .title--joint .title__small { font-size: 26px; margin: 0 7px; }
  .title--multi { left: 233px; top: 56px; font-size: 49px; letter-spacing: -0.6px; }
  .title__count { position: absolute; left: 443px; top: 110px; font-family: "Bebas Neue", sans-serif; font-size: 10px; color: var(--red); white-space: nowrap; }

  .tagline { position: absolute; font-family: "Bebas Neue", sans-serif; font-size: 18px; line-height: 19px; color: var(--ink); text-align: center; white-space: nowrap; }
  .tagline--probiotic { left: 317px; top: 128px; width: 120px; }
  .tagline--joint { left: 316px; top: 122px; width: 160px; font-size: 17px; letter-spacing: -0.2px; }
  .tagline--multi { left: 290px; top: 131px; width: 200px; text-align: right; }

  .blurb { position: absolute; left: 544px; top: 46px; width: 168px; font-size: 6.9px; line-height: 8.4px; color: var(--ink); }

  .badge { position: absolute; width: 32px; height: 32px; border-radius: 50%; background: var(--badge-light); border: 3px solid var(--badge-navy); }
  .seal { position: absolute; width: 44px; height: 29px; background: var(--white); border: 1px solid #dde3ee; }
</style>
</head>
<body>

  <section class="label label--probiotic">
    <div class="label__band-top"></div>
    <span class="brand__mark"></span><span class="brand__name">TOVEL CREST</span>
    <div class="serving">
      <div class="serving__title">SERVING SIZE</div>
      <table>
        <tr><th>Body Weight</th><th>Chews / Day</th></tr>
        <tr><td>Under 10 lbs</td><td>1</td></tr>
        <tr><td>10-30 lbs</td><td>2</td></tr>
        <tr><td>31-60 lbs</td><td>3</td></tr>
        <tr><td>61-90 lbs</td><td>4</td></tr>
        <tr><td>over 90lbs</td><td>5</td></tr>
      </table>
    </div>
    <div class="art art--dog" role="img" aria-label="Photo of a sitting golden retriever"></div>
    <div class="art art--cat" role="img" aria-label="Photo of a lying tabby cat"></div>
    <div class="title title--probiotic">PROBIOTIC</div>
    <div class="tagline tagline--probiotic">DIGESTIVE HEALTH<br>FOR CATS AND DOGS</div>
    <span class="badge" style="left:484px;top:47px"></span>
    <span class="badge" style="left:484px;top:89px"></span>
    <span class="badge" style="left:484px;top:129px"></span>
    <p class="blurb">Give your furry friend the gift of a balanced and thriving digestive system with our premium Probiotic for Pets. Specially formulated to support digestive health in cats, dogs, and other beloved pets, our carefully selected probiotic strains are perfect for pets of all sizes and ages.</p>
    <span class="seal" style="left:544px;top:131px"></span>
    <div class="label__band-bottom">PET SUPPLEMENT</div>
  </section>

  <section class="label label--joint">
    <div class="label__band-top"></div>
    <span class="brand__mark"></span><span class="brand__name">TOVEL CREST</span>
    <div class="serving">
      <div class="serving__title">SERVING SIZE</div>
      <table>
        <tr><th>Body Weight</th><th>Chews / Day</th></tr>
        <tr><td>Under 10 lbs</td><td>1</td></tr>
        <tr><td>10-30 lbs</td><td>2</td></tr>
        <tr><td>31-60 lbs</td><td>3</td></tr>
        <tr><td>61-90 lbs</td><td>4</td></tr>
        <tr><td>over 90lbs</td><td>5</td></tr>
      </table>
    </div>
    <div class="art art--dog" role="img" aria-label="Photo of a sitting golden retriever"></div>
    <div class="art art--cat" role="img" aria-label="Photo of a lying tabby cat"></div>
    <div class="title title--joint">HIP<span class="title__small">AND</span>JOINT</div>
    <div class="tagline tagline--joint">HELPING YOUR PET MOVE<br>WITH EASE AND COMFORT!</div>
    <p class="blurb">Give your four-legged friend the gift of mobility and comfort with our premium Hip and Joint Support for Pets. Specially formulated to promote joint health and alleviate discomfort, our carefully crafted blend of ingredients is perfect for cats, dogs, and other furry companions of all sizes and ages.</p>
    <span class="badge" style="left:545px;top:129px"></span>
    <span class="badge" style="left:585px;top:129px"></span>
    <span class="badge" style="left:629px;top:129px"></span>
    <span class="seal" style="left:670px;top:131px"></span>
    <div class="label__band-bottom">PET SUPPLEMENT</div>
  </section>

  <section class="label label--multi">
    <div class="label__band-top"></div>
    <span class="brand__mark"></span><span class="brand__name">TOVEL CREST</span>
    <div class="serving">
      <div class="serving__title">SERVING SIZE</div>
      <table>
        <tr><th>Body Weight</th><th>Chews / Day</th></tr>
        <tr><td>Under 10 lbs</td><td>1</td></tr>
        <tr><td>10-30 lbs</td><td>2</td></tr>
        <tr><td>31-60 lbs</td><td>3</td></tr>
        <tr><td>61-90 lbs</td><td>4</td></tr>
        <tr><td>over 90lbs</td><td>5</td></tr>
      </table>
    </div>
    <div class="art art--dog" role="img" aria-label="Photo of a sitting golden retriever"></div>
    <div class="art art--cat" role="img" aria-label="Photo of a lying tabby cat"></div>
    <div class="title title--multi">MULTIVITAMIN</div>
    <div class="title__count">(12 IN 1)</div>
    <div class="tagline tagline--multi">BOOST YOUR PET'S IMMUNITY<br>LUSTROUS COAT AND HEALTHY SKIN</div>
    <p class="blurb">Specially formulated to support the well-being of cats and dogs and small animals, our comprehensive blend of essential vitamins and minerals is the perfect addition to your pet's daily routine.</p>
    <span class="badge" style="left:545px;top:129px"></span>
    <span class="badge" style="left:585px;top:129px"></span>
    <span class="badge" style="left:629px;top:129px"></span>
    <span class="seal" style="left:670px;top:131px"></span>
    <div class="label__band-bottom">PET SUPPLEMENT</div>
  </section>

</body>
</html>
```